Yard Sign Design Needed

Yard sign needed for mowing & landscaping company. Would like to use the top logo with black background which is attached. Would like MOWING to be in large standout letters. The word "landscaping" can be smaller and more artistic or omitted. Will need room for phone number once design is approved. The phone number will need to stand out and look identical/similar to the word 'MOWING"

```html
<!DOCTYPE html>
<html lang="en">
<head>
<meta charset="UTF-8">
<title>Brevik Contractors – Mowing Yard Sign</title>
<link rel="stylesheet" href="https://fonts.googleapis.com/css2?family=Arimo:wght@700&display=swap">
<style>
  :root {
    --sign-green: #9db42a;
    --sign-black: #0c0c0c;
    --sign-white: #f4f4f4;
    --brand-green: #a6c12e;
  }
  html, body {
    margin: 0;
    padding: 0;
    width: 1200px;
    height: 1200px;
    overflow: hidden;
    background: #ffffff;
  }
  .yard-sign {
    position: relative;
    width: 1200px;
    height: 1200px;
    background: var(--sign-green);
    font-family: "Arimo", Arial, sans-serif;
    font-weight: 700;
    color: var(--sign-black);
    overflow: hidden;
  }
  .header-band {
    position: absolute;
    inset: 0 0 auto 0;
    width: 1200px;
    height: 440px;
  }
  .brand {
    position: absolute;
    top: 110px;
    left: 0;
    width: 1200px;
    display: flex;
    flex-direction: column;
    align-items: center;
    gap: 22px;
  }
  .brand-square {
    width: 90px;
    height: 90px;
    background: var(--brand-green);
  }
  .brand-name {
    color: var(--brand-green);
    font-size: 40px;
    letter-spacing: 3px;
    text-align: center;
    line-height: 1.15;
    margin: 0;
  }
  .service-main {
    position: absolute;
    top: 460px;
    left: 0;
    width: 1200px;
    margin: 0;
    text-align: center;
    font-size: 240px;
    line-height: 1;
    letter-spacing: -2px;
  }
  .service-sub {
    position: absolute;
    top: 730px;
    left: 0;
    width: 1200px;
    margin: 0;
    text-align: center;
    font-size: 90px;
    line-height: 1;
  }
  .phone-pill {
    position: absolute;
    top: 868px;
    left: 120px;
    width: 960px;
    height: 165px;
    background: var(--sign-black);
    border-radius: 28px;
    display: flex;
    align-items: center;
    justify-content: center;
  }
  .phone-number {
    color: var(--sign-white);
    font-size: 130px;
    line-height: 1;
    letter-spacing: -1px;
  }
  .website {
    position: absolute;
    top: 1062px;
    left: 0;
    width: 1200px;
    margin: 0;
    text-align: center;
    font-size: 72px;
    line-height: 1;
  }
</style>
</head>
<body>
  <main class="yard-sign">
    <svg class="header-band" viewBox="0 0 1200 440" aria-hidden="true">
      <polygon points="0,0 1200,0 1200,200 655,440 0,175" fill="var(--sign-black)"/>
    </svg>

    <div class="brand">
      <div class="brand-square"></div>
      <p class="brand-name">BREVIK<br>CONTRACTORS LLC</p>
    </div>

    <h1 class="service-main">MOWING</h1>
    <p class="service-sub">LANDSCAPING</p>

    <div class="phone-pill">
      <span class="phone-number">555-GRASSY</span>
    </div>

    <p class="website">www.brevikyard.com</p>
  </main>
</body>
</html>
```